custom carpentry, woodworking and home repair company needs logo design and business card design

Attention: I apologize but I just received notification from my state that I cannot use the company name that I originally submitted (Beyond The Bench). The new name will be Joinolux We need a company logo and business card design for our new company based in the Hampton Roads area of Virginia. The company name is Joinolux. The final design should give a first impression of true craftsmanship and attention to detail. We would like the card to include the company name, my name Mark Tellman (owner), phone number (757) 348-2615, website (joinolux-example.com) and email address (mark@joinolux-example.com). Everything else is up to your discretion. Thanks, have fun, and good luck.

Industry/Entity Type

Business

Contact Information for Business Card

See project description

Logo Text

see project description

Colors

Designer to choose colors to be used in the design.

```html
<!DOCTYPE html>
<html lang="en">
<head>
<meta charset="utf-8">
<title>Joinolux business card</title>
<link href="https://fonts.googleapis.com/css2?family=Questrial&display=swap" rel="stylesheet">
<style>
  :root {
    --stage: #686868;
    --paper: #ffffff;
    --charcoal: #1c1b1b;
    --walnut: #512d17;
    --ink-light: #ffffff;
  }
  html, body {
    margin: 0;
    width: 1200px;
    height: 976px;
    overflow: hidden;
    background: var(--stage);
    font-family: "Questrial", sans-serif;
  }
  .card {
    position: absolute;
    left: 327px;
    top: 274px;
    width: 571px;
    height: 342px;
    background: var(--paper);
    overflow: hidden;
  }
  .card__panels {
    position: absolute;
    inset: 0;
    width: 100%;
    height: 100%;
  }
  .brand-name {
    position: absolute;
    left: 0;
    width: 295px;
    top: 210px;
    margin: 0;
    text-align: center;
    font-size: 40px;
    font-weight: 400;
    letter-spacing: 1px;
    color: var(--walnut);
    line-height: 1;
  }
  .holder {
    position: absolute;
    right: 22px;
    top: 174px;
    margin: 0;
    text-align: right;
    color: var(--ink-light);
    line-height: 1;
  }
  .holder__name {
    display: block;
    font-size: 26px;
    font-weight: 400;
  }
  .holder__role {
    display: block;
    font-size: 20px;
    margin-top: 4px;
  }
  .contacts {
    position: absolute;
    right: 22px;
    top: 254px;
    margin: 0;
    padding: 0;
    list-style: none;
    color: var(--ink-light);
    font-size: 13px;
  }
  .contacts__item {
    display: flex;
    justify-content: flex-end;
    align-items: center;
    gap: 7px;
    height: 23.5px;
  }
  .contacts__icon {
    width: 13px;
    height: 13px;
    flex: none;
  }
</style>
</head>
<body>
  <article class="card">
    <svg class="card__panels" viewBox="0 0 666 399" preserveAspectRatio="none" aria-hidden="true">
      <defs>
        <linearGradient id="edge-shade" x1="0" x2="1" y1="0" y2="0">
          <stop offset="0" stop-color="#000" stop-opacity="0"/>
          <stop offset="1" stop-color="#000" stop-opacity="0.35"/>
        </linearGradient>
      </defs>
      <path d="M326,0 L348,0 Q365,80 370,190 Q360,300 344,399 L324,399 Q342,300 350,190 Q345,80 326,0 Z" fill="url(#edge-shade)"/>
      <path d="M348,0 H666 V399 H396 L370,190 Q365,80 348,0 Z" fill="var(--charcoal)"/>
      <path d="M370,190 L396,399 H344 Q360,300 370,190 Z" fill="var(--walnut)"/>
    </svg>

    <h1 class="brand-name">Joinolux</h1>

    <p class="holder">
      <span class="holder__name">Mark Tellman</span>
      <span class="holder__role">owner</span>
    </p>

    <ul class="contacts">
      <li class="contacts__item">(757) 348-2615
        <svg class="contacts__icon" viewBox="0 0 16 16" aria-hidden="true"><path d="M1 6 Q8 0 15 6 L13 8 L11 6 V5 H5 V6 L3 8 Z M4 9 H12 L14 14 H2 Z" fill="#fff"/></svg>
      </li>
      <li class="contacts__item">www.joinolux-example.com
        <svg class="contacts__icon" viewBox="0 0 16 16" aria-hidden="true"><g fill="none" stroke="#fff" stroke-width="1.3"><circle cx="8" cy="8" r="6.5"/><ellipse cx="8" cy="8" rx="3" ry="6.5"/><path d="M1.5 8H14.5M2.5 4.5H13.5M2.5 11.5H13.5"/></g></svg>
      </li>
      <li class="contacts__item">mark@joinolux-example.com
        <svg class="contacts__icon" viewBox="0 0 16 16" aria-hidden="true"><g fill="none" stroke="#fff" stroke-width="1.4"><rect x="1.5" y="3.5" width="13" height="9"/><path d="M1.5 3.5 L8 9 L14.5 3.5M1.5 12.5 L6 8M14.5 12.5 L10 8"/></g></svg>
      </li>
    </ul>
  </article>
</body>
</html>
```